dsadasdasdasdsa

Industry/Entity Type

Mortgage Broking

Requirements
Must have
• Call-to-action button somewhere on the graphic
Nice to have
• The font of our logo is Montserrat

```html
<!DOCTYPE html>
<html lang="en">
<head>
<meta charset="UTF-8">
<title>Mortgage Broker Directory Banner</title>
<link rel="stylesheet" href="https://fonts.googleapis.com/css2?family=Montserrat:wght@600;700;800;900&display=swap">
<style>
  :root {
    --forest: #1f6b3a;
    --forest-deep: #14532b;
    --mint-light: #f4fbef;
    --mint: #c9ecb2;
    --lime-yellow: #f6ef22;
    --white: #ffffff;
    --brick: #d2482a;
    --brick-deep: #b8351d;
    --button-text: #1d5a2c;
    --shell-brown: #8a5a2e;
    --shell-green: #6fae4a;
  }
  * { margin: 0; padding: 0; box-sizing: border-box; }
  html, body {
    width: 1200px;
    height: 180px;
    overflow: hidden;
    background: var(--white);
  }
  .banner {
    position: relative;
    width: 1200px;
    height: 180px;
    overflow: hidden;
    font-family: "Montserrat", sans-serif;
    background: linear-gradient(90deg, var(--mint-light) 55%, var(--mint) 85%);
  }
  .banner__shapes {
    position: absolute;
    inset: 0;
  }
  .banner__mascot {
    position: absolute;
    left: 705px;
    top: 8px;
    width: 205px;
    height: 172px;
    border-radius: 90px 90px 20px 20px;
    background: radial-gradient(circle at 50% 35%, var(--shell-green) 0%, #9fcf7c 45%, #c49a6c 75%, rgba(138,90,46,0.35) 100%);
  }
  .headline {
    position: absolute;
    left: 32px;
    top: 30px;
    color: var(--white);
  }
  .headline__question {
    display: block;
    font-weight: 600;
    font-size: 35px;
    line-height: 42px;
    color: var(--lime-yellow);
    letter-spacing: 0.2px;
  }
  .headline__action {
    display: block;
    font-weight: 800;
    font-size: 30px;
    line-height: 40px;
    text-transform: uppercase;
  }
  .headline__highlight {
    display: block;
    font-weight: 800;
    font-size: 40px;
    line-height: 44px;
    text-transform: uppercase;
  }
  .cta-button {
    position: absolute;
    left: 1012px;
    top: 75px;
    width: 170px;
    height: 46px;
    border-radius: 23px;
    background: var(--lime-yellow);
    color: var(--button-text);
    font-weight: 800;
    font-size: 18px;
    letter-spacing: 0.3px;
    display: flex;
    align-items: center;
    justify-content: center;
    text-decoration: none;
    text-transform: uppercase;
    box-shadow: 0 2px 4px rgba(0,0,0,0.15);
  }
</style>
</head>
<body>
  <div class="banner">
    <svg class="banner__shapes" width="1200" height="180" viewBox="0 0 1200 180" aria-hidden="true">
      <defs>
        <linearGradient id="forestFill" x1="0" y1="0" x2="1" y2="0">
          <stop offset="0" stop-color="var(--forest-deep)"/>
          <stop offset="1" stop-color="var(--forest)"/>
        </linearGradient>
        <linearGradient id="brickFill" x1="0" y1="0" x2="1" y2="0">
          <stop offset="0" stop-color="var(--brick)"/>
          <stop offset="1" stop-color="var(--brick-deep)"/>
        </linearGradient>
      </defs>
      <path class="panel-message" d="M0 0 H645 L690 90 L645 180 H0 Z" fill="url(#forestFill)"/>
      <path class="panel-action" d="M1010 0 H1200 V180 H1010 L965 90 Z" fill="url(#brickFill)"/>
    </svg>

    <div class="banner__mascot" role="img" aria-label="Cartoon turtle mascot holding a small house"></div>

    <h1 class="headline">
      <span class="headline__question">Need a Mortgage Broker?</span>
      <span class="headline__action">Search now on Australia’s</span>
      <span class="headline__highlight">Largest Directory</span>
    </h1>

    <a class="cta-button" href="#">Click here</a>
  </div>
</body>
</html>
```